Whitmore Business Card Design

The name of the business is Dara Whitmore, CPA LLC
The service that we offer is Accounting, Tax & Consulting Services. I need it to have the following items:
Dara Whitmore, Principal
Phone Number
Email Address
Physical Address

I have attached the company logo, one in black and one in white. Please provide a design in black background and the other in white background. Please include "Accounting, Tax & Consulting Services". I want the business card to be clean and very professional.

```html
<!DOCTYPE html>
<html lang="en">
<head>
<meta charset="utf-8">
<title>Dara Whitmore, CPA LLC — Business Cards</title>
<link href="https://fonts.googleapis.com/css2?family=Poppins:wght@300;400;500;600&display=swap" rel="stylesheet">
<style>
  :root {
    --brand-red: #961e21;
    --charcoal: #3a3a3d;
    --night: #1b1e20;
    --slate-grey: #8d8d8f;
    --paper: #ffffff;
  }
  html, body {
    margin: 0;
    padding: 0;
    width: 1200px;
    height: 1000px;
    overflow: hidden;
    background: var(--paper);
    font-family: "Poppins", sans-serif;
  }
  .card {
    position: absolute;
    left: 317px;
    width: 565px;
    height: 340px;
    display: block;
  }
  .card--front { top: 122px; }
  .card--back { top: 532px; }
  .card text { font-family: "Poppins", sans-serif; }
  .firm-name { font-weight: 600; }
  .firm-role { font-weight: 500; letter-spacing: 3px; }
  .firm-services { font-weight: 400; }
  .contact-line { font-weight: 300; letter-spacing: 1px; }
  .web-line { font-weight: 400; letter-spacing: 3px; }
</style>
</head>
<body>

<!-- Front: white card -->
<svg class="card card--front" viewBox="0 0 942 566" xmlns="http://www.w3.org/2000/svg" aria-label="Front of business card">
  <rect width="942" height="566" fill="var(--paper)"/>
  <rect class="top-band" width="942" height="32" fill="var(--charcoal)"/>
  <path class="corner-wave" d="M710,32 C770,95 820,125 870,121 C905,118 925,108 942,96 V32 Z" fill="var(--charcoal)"/>
  <path class="base-wave" d="M0,468 C30,450 60,442 90,446 C140,452 190,500 232,534 H942 V566 H0 Z" fill="var(--brand-red)"/>

  <rect class="brand-square" x="198" y="252" width="22" height="22" fill="var(--brand-red)"/>
  <text class="firm-name" x="486" y="274" text-anchor="middle" font-size="38" fill="var(--charcoal)">Dara Whitmore, CPA LLC</text>
  <text class="firm-role" x="471" y="318" text-anchor="middle" font-size="24" fill="var(--slate-grey)">CERTIFIED PUBLIC ACCOUNTANT</text>
  <text class="firm-services" x="471" y="394" text-anchor="middle" font-size="24" fill="var(--brand-red)">Accounting, Tax &amp; Consulting Services</text>

  <g class="web-icon" transform="translate(347,492)">
    <circle r="12" fill="var(--brand-red)"/>
    <circle r="6.5" fill="none" stroke="#fff" stroke-width="1.2"/>
    <ellipse rx="3" ry="6.5" fill="none" stroke="#fff" stroke-width="1.2"/>
    <line x1="-6.5" y1="0" x2="6.5" y2="0" stroke="#fff" stroke-width="1.2"/>
  </g>
  <text class="web-line" x="380" y="499" font-size="21" fill="var(--brand-red)">www.website.com</text>
</svg>

<!-- Back: dark card -->
<svg class="card card--back" viewBox="0 0 942 566" xmlns="http://www.w3.org/2000/svg" aria-label="Back of business card">
  <rect width="942" height="566" fill="var(--night)"/>
  <rect class="top-band" width="942" height="31" fill="var(--brand-red)"/>

  <rect class="name-accent" x="60" y="142" width="15" height="78" fill="var(--brand-red)"/>
  <text x="99" y="177" font-size="42" fill="#fff" letter-spacing="1"><tspan font-weight="500">DARA</tspan><tspan font-weight="300"> WHITMORE</tspan></text>
  <text x="99" y="220" font-size="25" font-weight="400" fill="#fff" letter-spacing="1">Principal</text>
  <line class="title-rule" x1="236" y1="218" x2="432" y2="218" stroke="var(--brand-red)" stroke-width="2.5"/>

  <rect class="brand-square" x="692" y="190" width="22" height="22" fill="var(--brand-red)"/>
  <text class="firm-name" x="712" y="262" text-anchor="middle" font-size="25" fill="#fff">Dara Whitmore, CPA LLC</text>
  <text class="firm-role" x="712" y="288" text-anchor="middle" font-size="17" fill="var(--slate-grey)" letter-spacing="2">CERTIFIED PUBLIC ACCOUNTANT</text>
  <text class="firm-services" x="712" y="319" text-anchor="middle" font-size="16" fill="#fff">Accounting, Tax &amp; Consulting Services</text>

  <path class="left-wave" d="M0,368 C70,330 140,318 200,326 C330,343 460,460 545,566 H0 Z" fill="var(--brand-red)"/>
  <path class="right-wave" d="M459,425 C520,450 600,450 680,432 C760,412 820,400 870,412 C900,420 925,432 942,442 V566 H585 C545,510 500,460 459,425 Z" fill="var(--brand-red)"/>

  <g class="phone-icon" transform="translate(72,388)">
    <circle r="12" fill="#fff"/>
    <path d="M-5,-5 L-2,-6 L0,-2 L-2,-1 C-1,1 1,3 2,3 L3,1 L6,3 L5,6 C-1,6 -6,1 -5,-5 Z" fill="var(--brand-red)"/>
  </g>
  <text class="contact-line" x="104" y="396" font-size="21" fill="#fff">+001 234 5678</text>

  <g class="mail-icon" transform="translate(72,439)">
    <circle r="12" fill="#fff"/>
    <rect x="-6" y="-4" width="12" height="8" fill="var(--brand-red)"/>
    <polyline points="-6,-4 0,1 6,-4" fill="none" stroke="#fff" stroke-width="1.2"/>
  </g>
  <text class="contact-line" x="104" y="447" font-size="21" fill="#fff">username@email.com</text>

  <g class="pin-icon" transform="translate(72,493)">
    <circle r="12" fill="#fff"/>
    <path d="M0,7 C-4,2 -5,0 -5,-2 A5,5 0 0 1 5,-2 C5,0 4,2 0,7 Z" fill="var(--brand-red)"/>
    <circle cy="-2" r="1.8" fill="#fff"/>
  </g>
  <text class="contact-line" x="104" y="501" font-size="21" fill="#fff">Street address,1234,City</text>

  <g class="web-icon" transform="translate(594,492)">
    <circle r="12" fill="#fff"/>
    <circle r="6.5" fill="none" stroke="var(--brand-red)" stroke-width="1.2"/>
    <ellipse rx="3" ry="6.5" fill="none" stroke="var(--brand-red)" stroke-width="1.2"/>
    <line x1="-6.5" y1="0" x2="6.5" y2="0" stroke="var(--brand-red)" stroke-width="1.2"/>
  </g>
  <text class="web-line" x="627" y="500" font-size="21" fill="#fff" letter-spacing="2">www.website.com</text>
</svg>

</body>
</html>
```